Defense Attorney Business Card Design Project/ Stationary

I am looking for a distinctive business card design for my solo law practice.
I practice criminal defense, both juvenile and adult, including DUI. I am a very experienced attorney with prior military experience. The design should convey a traditional, old school flair, but not be too stodgy or uptight. Some color. My logo should appear.

Project Deadline Extended Reason: I misunderstood how this project works and I was not prepared with my logo when this project ran the first time. Added Thursday, November 13, 2014

Reason: I was sent overseas on military duty last year, which interrupted this project. Thank you for your participation... I hope we can get this done this week! Thank you, Des

Target Market(s)

Regular everyday people looking for strong, knowledgeable, authoritative representation while they are faced with criminal charges. Many have never been charged with a crime before. A reassuring air is therefore desired.

Industry/Entity Type

Business

Contact Information for Business Card

My information is:
Desmond R. Whitcombe, Attorney at Law
735 Linden Avenue Suite 300
Oakland, California 94618
Tel: (510) 555-0183
Fax: (510) 555-0162
email: deswhitcombelaw@mailbrook.net
web: www.deswhitcombelaw.net

Font styles to use
Serif
Sans Serif
Decorative

Colors
0255a3
ffffff

Requirements
Must have
• Sharp lines, bold elements. Conservative use of colors, such as deep blues, burgundy, grays for example.
• While my logo says "Des Whitcombe", it should be modified to show "Desmond R. Whitcombe".
Should not have
• Cliche imagery such as scales of justice, gavels, Tower of Varenholt, etc.

```html
<!DOCTYPE html>
<html lang="en">
<head>
<meta charset="utf-8">
<title>Desmond R. Whitcombe — Business Card</title>
<link rel="stylesheet" href="https://fonts.googleapis.com/css2?family=Cinzel:wght@500;600&family=Cabin:wght@400;500&display=swap">
<style>
  :root {
    --backdrop: #b9b8b8;
    --burgundy: #7a0912;
    --burgundy-mid: #8c1320;
    --burgundy-light: #9a1c28;
    --gold: #d9a81c;
    --gold-light: #f0d43a;
    --gold-deep: #c08a1a;
    --ink: #2b2b2b;
    --paper: #ffffff;
  }
  * { margin: 0; padding: 0; box-sizing: border-box; }
  html, body { width: 1200px; height: 1000px; overflow: hidden; }
  body { background: var(--backdrop); position: relative; font-family: "Cabin", sans-serif; }

  /* Front of card */
  .card-front {
    position: absolute; left: 55px; top: 40px; width: 768px; height: 427px;
    background: linear-gradient(90deg, var(--burgundy) 0%, var(--burgundy-light) 35%, var(--burgundy-mid) 55%, var(--burgundy) 100%);
  }
  .emblem-area {
    position: absolute; left: 190px; top: 58px; width: 400px; height: 205px;
    background: linear-gradient(100deg, var(--gold-deep) 0%, var(--gold-light) 45%, var(--gold) 100%);
    border-radius: 6px; opacity: .9;
  }
  .front-name {
    position: absolute; left: 107px; width: 533px; top: 262px; text-align: center;
    font-family: "Cinzel", serif; font-weight: 600; font-size: 36px; letter-spacing: .5px;
    color: var(--gold); white-space: nowrap;
  }
  .front-rule {
    position: absolute; left: 107px; top: 321px; width: 533px; height: 2px; background: var(--gold);
  }
  .front-title {
    position: absolute; left: 107px; width: 533px; top: 330px; text-align: center;
    font-family: "Cinzel", serif; font-weight: 500; font-size: 27px; letter-spacing: 2px;
    color: var(--gold);
  }
  .front-title .small { font-size: 19px; }

  /* Back of card */
  .card-back {
    position: absolute; left: 383px; top: 541px; width: 772px; height: 417px;
    background: var(--paper);
  }
  .ribbon {
    position: absolute; left: 27px; top: 0; width: 146px; height: 404px;
  }
  .ribbon svg { display: block; }
  .ribbon-emblem {
    position: absolute; left: 18px; top: 246px; width: 110px; height: 50px;
    background: linear-gradient(100deg, var(--gold-deep), var(--gold-light), var(--gold));
    border-radius: 3px;
  }
  .ribbon-title {
    position: absolute; left: 0; width: 146px; top: 310px; text-align: center;
    font-size: 20px; line-height: 26px; color: var(--gold-light);
  }
  .back-name {
    position: absolute; right: 40px; top: 176px;
    font-weight: 400; font-size: 44px; color: var(--ink); white-space: nowrap;
  }
  .back-rule {
    position: absolute; left: 204px; top: 239px; width: 526px; height: 2px; background: var(--burgundy);
  }
  .contact {
    position: absolute; right: 37px; top: 278px; text-align: right;
    font-weight: 500; font-size: 18px; line-height: 25.5px; color: var(--burgundy);
    white-space: nowrap;
  }
  .contact .phones span + span { margin-left: 60px; }
  .edge-tab {
    position: absolute; right: -3px; top: 284px; width: 28px; height: 89px; background: var(--burgundy);
  }
</style>
</head>
<body>
  <section class="card-front">
    <div class="emblem-area" role="img" aria-label="Gold emblem illustration area"></div>
    <div class="front-name">Desmond R. Whitcombe</div>
    <div class="front-rule"></div>
    <div class="front-title">ATTORNEY <span class="small">AT</span> LAW</div>
  </section>

  <section class="card-back">
    <div class="ribbon">
      <svg width="146" height="404" viewBox="0 0 146 404">
        <defs>
          <linearGradient id="ribbonFill" x1="0" y1="0" x2="0" y2="1">
            <stop offset="0" stop-color="#7a0912"/>
            <stop offset=".5" stop-color="#941a26"/>
            <stop offset="1" stop-color="#7a0912"/>
          </linearGradient>
        </defs>
        <path d="M1.5 0 V360 L73 402 L144.5 360 V0" fill="url(#ribbonFill)" stroke="#d9a81c" stroke-width="3"/>
      </svg>
      <div class="ribbon-emblem" role="img" aria-label="Small gold emblem illustration area"></div>
      <div class="ribbon-title">ATTORNEY<br>AT LAW</div>
    </div>
    <h1 class="back-name">Desmond R. Whitcombe</h1>
    <div class="back-rule"></div>
    <address class="contact" style="font-style:normal">
      <div>735 Linden Avenue Suite 300 Oakland, California 94618</div>
      <div class="phones"><span>t. (510) 555-0183</span><span>f. (510) 555-0162</span></div>
      <div>deswhitcombelaw@mailbrook.net</div>
      <div>www.deswhitcombelaw.net</div>
    </address>
    <div class="edge-tab"></div>
  </section>
</body>
</html>
```